Business Card Design Project

We need a Business Card for an Mechanical Engineering firm in Singapore. The design should be Modern & Technical looking, yet eye catching.

Our company deals in Cutting Tools & Machine Accessories for the Manufacturing Industries such as Oil & Gas, Aero Space, etc... For more information on our Company, you can either email me or view our website www.valtrion.com.sg.

We are trying to revamp our image to give our consumers a fresh new perspective to our company, so we welcome all ideas.

Industry/Entity Type

Business

Requirements
Must have
• Must incorporate New Company Logo into the card as shown in Uploaded file.

```html
<!DOCTYPE html>
<html lang="en">
<head>
<meta charset="utf-8">
<title>Valtrion Tools – Business Card</title>
<link rel="stylesheet" href="https://fonts.googleapis.com/css2?family=Mulish:wght@400;700&display=swap">
<style>
  :root {
    --backdrop: #a9b298;
    --card-maroon: #8e0030;
    --card-white: #ffffff;
    --ink-light: #ffffff;
    --ink-maroon: #8e0030;
    --card-shadow: rgba(30, 35, 20, 0.35);
  }
  * { box-sizing: border-box; margin: 0; padding: 0; }
  html, body {
    width: 1200px;
    height: 900px;
    overflow: hidden;
  }
  body {
    background: var(--backdrop);
    font-family: "Mulish", sans-serif;
    position: relative;
  }
  .card {
    position: absolute;
    top: 315px;
    width: 490px;
    height: 270px;
    border-radius: 24px;
    box-shadow: 0 6px 14px var(--card-shadow);
  }
  .card-front {
    left: 80px;
    background: var(--card-maroon);
    color: var(--ink-light);
  }
  .card-back {
    left: 630px;
    background: var(--card-white);
    display: flex;
    align-items: center;
    justify-content: center;
  }
  .front-brand {
    position: absolute;
    left: 52px;
    top: 150px;
    display: flex;
    align-items: center;
    gap: 8px;
    font-size: 14px;
    font-weight: 400;
    color: var(--ink-light);
  }
  .brand-dot {
    width: 22px;
    height: 22px;
    border-radius: 50%;
    background: var(--ink-light);
  }
  .holder-name {
    position: absolute;
    left: 198px;
    top: 76px;
    font-size: 23px;
    font-weight: 700;
  }
  .contact-list {
    position: absolute;
    left: 198px;
    top: 138px;
    list-style: none;
    font-size: 16px;
    line-height: 20px;
  }
  .address {
    position: absolute;
    left: 0;
    right: 0;
    top: 236px;
    text-align: center;
    font-size: 13.5px;
  }
  .back-brand {
    display: flex;
    align-items: center;
    gap: 12px;
    font-size: 30px;
    font-weight: 700;
    color: var(--ink-maroon);
  }
  .back-brand .brand-dot {
    width: 34px;
    height: 34px;
    background: var(--ink-maroon);
  }
</style>
</head>
<body>
  <section class="card card-front">
    <div class="front-brand">
      <span class="brand-dot"></span>
      <span>Valtrion Tools</span>
    </div>
    <h1 class="holder-name">Daniel Tan</h1>
    <ul class="contact-list">
      <li>tel: 656 555 0142</li>
      <li>mob: 123 555 0190</li>
      <li>hello@valtrion.com.sg</li>
      <li>www.valtrion.com.sg</li>
    </ul>
    <p class="address">27 Kallang Way #03-12, Meridian Industrial Hub, Singapore 349201</p>
  </section>

  <section class="card card-back">
    <div class="back-brand">
      <span class="brand-dot"></span>
      <span>Valtrion Tools</span>
    </div>
  </section>
</body>
</html>
```